Quirky Coffee Shop Loyalty Card

We need a new loyalty card in business card size format for our independent coffee shop. We are a quirky, ethically focussed, high quality coffee establishment with a focus on cutting edge products like siphon coffee and flamed latte brules. Projecting an image of high quality, innovation, ethical and eco-friendly with a quirky and unique feel. We would like a green background appearance, echoing or complementing the green in our logo (uploaded). Our coffee is organic and ethically sourced, we would like to communicate this - it doesn't need to be done in obvious way, open to creative suggestions. Earthy and straightforward in approach is important to us. We use cups made from 100% repurposed coffee husk, called Brindle (https://brindlecups.example/). One idea we had would be to have this cup image on the card with arrows pointing in from words like "Organic", "Made from coffee husks", "Ethical" etc... but in a less cliche'd way than this sounds!Please note that although this is a business card size, we need a loyalty card not a business card. On the back, we need to convey that the customer buys 8 coffees and gets the ninth free. We also need our social media links, email and address:
FB: @pebblekettlemossford
Insta: Pebblekettle
Email: mossford@pebblekettle.example
Address: No.4 Quill Row, ZX40 9KT
Phone: 01999 462057

Target Market(s)

All shop customers

Industry/Entity Type

Coffee Shop

Contact Information for Business Card

FB: @pebblekettlemossford
Insta: Pebblekettle
Phone: 01999 462057

Colors

Designer to choose colors to be used in the design.

Requirements
Must have
• Quirky, ethical, organic feel
Should not have
• Well-used or obvious coffee shop imagery

```html
<!DOCTYPE html>
<html lang="en">
<head>
<meta charset="utf-8">
<title>Pebblekettle Loyalty Card</title>
<link rel="stylesheet" href="https://fonts.googleapis.com/css2?family=Bebas+Neue&family=Open+Sans:wght@400;600&family=Raleway:wght@500&display=swap">
<style>
  :root {
    --backdrop: #3a2418;
    --card: #ffffff;
    --stamp: #d4d4d6;
    --brown: #8a4216;
    --brown-dark: #3b1e0e;
    --green: #6ab023;
    --ink: #2f2f2f;
    --black: #111111;
  }
  * { margin: 0; padding: 0; box-sizing: border-box; }
  html, body { width: 1200px; height: 900px; overflow: hidden; }
  body { background: var(--backdrop); position: relative; font-family: "Open Sans", sans-serif; }

  .card { position: absolute; background: var(--card); overflow: hidden; }
  .card-back { left: 330px; top: 90px; width: 555px; height: 343px; }
  .card-front { left: 330px; top: 469px; width: 559px; height: 344px; }

  .stamps { position: absolute; left: 32px; top: 25px; display: flex; gap: 4px; }
  .stamp { width: 42px; height: 42px; border-radius: 50%; background: var(--stamp);
    display: flex; align-items: center; justify-content: center;
    font: 600 12px "Open Sans", sans-serif; color: var(--ink); }

  .offer { position: absolute; left: 35px; top: 74px; font: 25px "Bebas Neue", sans-serif;
    color: var(--brown); letter-spacing: 0.3px; }

  .contacts { position: absolute; left: 24px; top: 150px; font-size: 15.5px; color: var(--ink); }
  .contact-row { display: flex; align-items: center; gap: 6px; height: 27px; }
  .contact-row + .contact-row { margin-top: 2px; }
  .contact-row.address { margin-top: 11px; }
  .dot { width: 22px; height: 22px; border-radius: 50%; background: var(--brown); flex: none;
    display: flex; align-items: center; justify-content: center; }
  .dot.plain { background: #7a7a7a; }
  .gap { width: 8px; }

  .brand-seal { position: absolute; left: 371px; top: 111px; width: 140px; height: 140px;
    border: 3px solid var(--brown); border-radius: 50%;
    display: flex; align-items: center; justify-content: center;
    font: 28px "Bebas Neue", sans-serif; color: var(--green); letter-spacing: 0.5px; }

  .rule { position: absolute; left: 24px; top: 277px; width: 497px; height: 2px; background: var(--brown); }

  .call { position: absolute; left: 0; right: 0; top: 284px; text-align: center;
    font: 44px "Bebas Neue", sans-serif; color: var(--green); word-spacing: 14px; }

  .cup-photo { position: absolute; inset: 0;
    background: linear-gradient(90deg, #d8d6d2 0%, #a9abad 25%, #e9ecee 45%, #f4f6f7 70%, #eef0f1 100%); }

  .husk-claim { position: absolute; left: 218px; top: 82px; width: 320px; text-align: center;
    font: 26px/32px "Bebas Neue", sans-serif; color: var(--brown-dark); }
  .husk-link { position: absolute; left: 218px; top: 182px; width: 320px; text-align: center;
    font: 500 16px "Raleway", sans-serif; color: var(--green); }
  .organic-arrow { position: absolute; left: 234px; top: 234px; }
  .organic { position: absolute; left: 352px; top: 224px; font: 42px "Bebas Neue", sans-serif; color: var(--black); }
</style>
</head>
<body>

<section class="card card-back">
  <div class="stamps">
    <span class="stamp"></span><span class="stamp"></span><span class="stamp"></span><span class="stamp"></span>
    <span class="stamp"></span><span class="stamp"></span><span class="stamp"></span><span class="stamp"></span>
    <span class="stamp">FREE</span>
  </div>
  <p class="offer">Buys 8 coffees and gets the ninth free.</p>

  <div class="contacts">
    <div class="contact-row">
      <span class="dot plain"></span><span>@pebblekettlemossford</span>
      <span class="gap"></span>
      <span class="dot plain"></span><span>Pebblekettle</span>
    </div>
    <div class="contact-row">
      <span class="dot">
        <svg width="12" height="9" viewBox="0 0 12 9"><rect x="0.5" y="0.5" width="11" height="8" fill="none" stroke="#fff"/><path d="M0.5 0.5 L6 5 L11.5 0.5" fill="none" stroke="#fff"/></svg>
      </span>
      <span>mossford@pebblekettle.example</span>
    </div>
    <div class="contact-row address">
      <span class="dot">
        <svg width="10" height="13" viewBox="0 0 10 13"><path d="M5 0.5 A4.5 4.5 0 0 1 9.5 5 C9.5 8 5 12.5 5 12.5 C5 12.5 0.5 8 0.5 5 A4.5 4.5 0 0 1 5 0.5Z" fill="#fff"/><circle cx="5" cy="5" r="1.7" fill="#8a4216"/></svg>
      </span>
      <span>No.4 Quill Row, ZX40 9KT</span>
    </div>
  </div>

  <div class="brand-seal">Pebblekettle</div>
  <div class="rule"></div>
  <p class="call">Call 01999 462057</p>
</section>

<section class="card card-front">
  <div class="cup-photo" role="img" aria-label="Photo of stacked cream and charcoal ribbed husk cups by a bright window"></div>
  <p class="husk-claim">We use cups made from 100%<br>repurposed coffee husk,<br>called Brindle</p>
  <p class="husk-link">www.brindlecups.example</p>
  <svg class="organic-arrow" width="116" height="28" viewBox="0 0 116 28">
    <rect x="0" y="12" width="90" height="4" fill="#8a4216"/>
    <path d="M80 2 L114 14 L80 26 Z" fill="#8a4216"/>
  </svg>
  <p class="organic">Organic</p>
</section>

</body>
</html>
```